Business Card Re-design

We are looking for a fresh bold look for general office business cards. We are a staffing agency that staffs industrial, coal mining, and clerical jobs.
Tag Line: We match the RIGHT talent to the RIGHT roles.
Halvern Office: 437 W. Hollowmere Ave, Halvern, KS - 47298
p. 812.555.0183 f. 812.555.0196
Corwick Office: 926 S. Larkfen Way, Corwick, KS - 47231
p. 812.555.0127 f. 812.555.0196
Absentee/Emergency 24hr Hotline 812.555.0164 opt.1
www.tallowcrestworkforce.example

```html
<!DOCTYPE html>
<html lang="en">
<head>
<meta charset="utf-8">
<title>Tallowcrest Workforce – Business Cards</title>
<link rel="stylesheet" href="https://fonts.googleapis.com/css2?family=Oswald:wght@500&family=Lato:wght@400;700&display=swap">
<style>
  :root {
    --stage: #2b2b2d;
    --paper: #ffffff;
    --navy: #0f3a66;
    --navy-ink: #123e6c;
    --green: #3f9b3a;
    --green-light: #7cc24a;
    --on-navy: #e8eef5;
    --tag-grey: #5a6b7c;
  }
  * { box-sizing: border-box; margin: 0; padding: 0; }
  html, body { width: 1200px; height: 997px; overflow: hidden; }
  body {
    background: var(--stage);
    font-family: "Lato", Arial, sans-serif;
    display: flex;
    flex-direction: column;
    align-items: center;
    justify-content: center;
    gap: 56px;
  }
  .card {
    width: 700px;
    height: 400px;
    background: var(--paper);
    display: flex;
    overflow: hidden;
    box-shadow: 0 12px 30px rgba(0,0,0,.45);
  }
  .panel-navy { background: var(--navy); color: var(--on-navy); }

  /* Back card: offices + tagline */
  .card-back .offices {
    width: 210px;
    padding: 0 0 0 34px;
    display: flex;
    flex-direction: column;
    justify-content: center;
    gap: 26px;
    font-size: 14px;
    line-height: 1.45;
  }
  .office-title {
    color: var(--green-light);
    text-decoration: underline;
    text-transform: uppercase;
    font-size: 14px;
    letter-spacing: .3px;
  }
  .card-back .brand-side {
    flex: 1;
    position: relative;
    display: flex;
    align-items: center;
    justify-content: center;
  }
  .tagline {
    position: absolute;
    right: 34px;
    bottom: 40px;
    font-size: 14px;
    color: var(--tag-grey);
  }
  .tagline strong { color: var(--green); font-weight: 700; }

  /* Brand name stand-in */
  .brand {
    display: flex;
    align-items: center;
    gap: 16px;
  }
  .brand-square {
    width: 26px;
    height: 26px;
    background: var(--navy-ink);
    flex: none;
  }
  .brand-name {
    font-family: "Oswald", "Arial Narrow", sans-serif;
    font-weight: 500;
    color: var(--navy-ink);
    text-transform: uppercase;
    font-size: 42px;
    line-height: 1;
    letter-spacing: 1px;
  }

  /* Front card: brand + contacts */
  .card-front .brand-side {
    width: 420px;
    display: flex;
    align-items: center;
    justify-content: center;
  }
  .card-front .contacts {
    flex: 1;
    display: flex;
    flex-direction: column;
    justify-content: center;
    align-items: flex-end;
    padding: 0 26px;
    font-size: 14px;
    gap: 6px;
  }
  .contact-line {
    display: flex;
    align-items: center;
    gap: 8px;
  }
  .contact-icon { width: 16px; height: 16px; flex: none; }
  .email-line { margin-top: 14px; font-size: 13px; }
  .web-line { color: var(--green-light); font-weight: 700; font-size: 14px; }
</style>
</head>
<body>

  <section class="card card-back">
    <div class="offices panel-navy">
      <div class="office">
        <div class="office-title">Halvern Office</div>
        <div>437 W. Hollowmere Ave</div>
        <div>Halvern, KS - 47298</div>
      </div>
      <div class="office">
        <div class="office-title">Corwick Office</div>
        <div>926 S. Larkfen Way</div>
        <div>Corwick, KS - 47231</div>
      </div>
    </div>
    <div class="brand-side">
      <div class="brand">
        <span class="brand-square"></span>
        <span class="brand-name">Tallowcrest<br>Workforce</span>
      </div>
      <p class="tagline">We match the RIGHT talent <strong>to the RIGHT roles.</strong></p>
    </div>
  </section>

  <section class="card card-front">
    <div class="brand-side">
      <div class="brand">
        <span class="brand-square"></span>
        <span class="brand-name">Tallowcrest<br>Workforce</span>
      </div>
    </div>
    <div class="contacts panel-navy">
      <div class="contact-line">812.555.0127
        <svg class="contact-icon" viewBox="0 0 16 16" aria-hidden="true"><circle cx="8" cy="8" r="7.3" fill="none" stroke="currentColor" stroke-width="1"/><path d="M5.2 4.3l1.3-.3.8 1.8-.9.7a5 5 0 0 0 2.1 2.1l.7-.9 1.8.8-.3 1.3c-3 .3-5.8-2.5-5.5-5.5z" fill="currentColor"/></svg>
      </div>
      <div class="contact-line">812.555.0196
        <svg class="contact-icon" viewBox="0 0 16 16" aria-hidden="true"><circle cx="8" cy="8" r="7.3" fill="none" stroke="currentColor" stroke-width="1"/><path d="M5.2 4.3l1.3-.3.8 1.8-.9.7a5 5 0 0 0 2.1 2.1l.7-.9 1.8.8-.3 1.3c-3 .3-5.8-2.5-5.5-5.5z" fill="currentColor"/></svg>
      </div>
      <div class="contact-line">tallowcrestworkforce.example
        <svg class="contact-icon" viewBox="0 0 16 16" aria-hidden="true"><circle cx="8" cy="8" r="7.3" fill="none" stroke="currentColor" stroke-width="1"/><rect x="4.3" y="5.3" width="7.4" height="5.4" fill="none" stroke="currentColor" stroke-width="1"/><path d="M4.3 5.3L8 8.3l3.7-3" fill="none" stroke="currentColor" stroke-width="1"/></svg>
      </div>
      <div class="contact-line">
        <svg class="contact-icon" viewBox="0 0 16 16" aria-hidden="true"><circle cx="8" cy="8" r="7.3" fill="none" stroke="currentColor" stroke-width="1"/><circle cx="8" cy="8" r="3.6" fill="none" stroke="currentColor" stroke-width="1"/><path d="M4.4 8h7.2M8 4.4v7.2" stroke="currentColor" stroke-width=".8"/></svg>
      </div>
      <div class="contact-line email-line">mdrayton@tallowcrestworkforce.example</div>
      <div class="contact-line web-line">www.tallowcrestworkforce.example</div>
    </div>
  </section>

</body>
</html>
```